Tallow Creek Architectural Systems Business Card

We have a logo - but we need a business card. We are a specialty manufacturer of wood wall and ceiling panels. Please visit our website - www.tallowcreekas.com to see examples of our products.
We create wood architectural systems - so we would love to see wood on the card somehow. Maybe something similar to our grille system?
We would like a spot on the business card for a QR code that people can scan to add the contact to their phone (we have the QR codes - just need a spot on the card).
As for the contact info - we want to keep it simple. (Name, Cell phone, Fax, email, website)

Target Market(s)

Architects and general contractors

Industry/Entity Type

Construction

Contact Information for Business Card

Name, Cell phone, fax, email, website

Requirements
Must have
• space for a QR code, wood feature
Nice to have
• We just want something a little different - but not too crazy. We want to stand out - but in a professional way.
Should not have
• nothing too busy

```html
<!DOCTYPE html>
<html lang="en">
<head>
<meta charset="utf-8">
<title>Tallow Creek Architectural Systems – Business Card</title>
<link href="https://fonts.googleapis.com/css2?family=Carlito:wght@400;700&display=swap" rel="stylesheet">
<style>
  :root {
    --backdrop: #2b2a2b;
    --brand-red: #b30404;
    --paper: #ffffff;
    --ink: #1e1e1e;
    --wood-light: #8a5634;
    --wood-mid: #6e4226;
    --wood-dark: #4e2e19;
  }
  * { margin: 0; padding: 0; box-sizing: border-box; }
  html, body { width: 887px; height: 1200px; overflow: hidden; }
  body {
    background: var(--backdrop);
    font-family: "Carlito", "Calibri", sans-serif;
    position: relative;
  }
  .card { position: absolute; left: 0; width: 887px; overflow: hidden; }

  /* Front face */
  .card-front { top: 4px; height: 574px; border-radius: 38px; background: var(--paper); }
  .wood-panel {
    position: absolute; left: 0; width: 100%;
    background: linear-gradient(180deg, var(--wood-mid) 0%, var(--wood-light) 45%, var(--wood-dark) 100%);
  }
  .wood-top { top: 0; height: 179px; }
  .wood-bottom { top: 395px; height: 179px; }
  .red-rule { position: absolute; left: 0; width: 100%; height: 8px; background: var(--brand-red); }
  .rule-top { top: 179px; }
  .rule-bottom { top: 387px; }
  .brand-band {
    position: absolute; top: 187px; left: 0; width: 100%; height: 200px;
    display: flex; align-items: center; justify-content: center; gap: 22px;
  }
  .brand-mark { width: 62px; height: 62px; background: var(--brand-red); }
  .brand-name {
    color: var(--brand-red); font-weight: 700; font-size: 31px; line-height: 1.1;
    text-transform: uppercase; letter-spacing: 1px;
  }

  /* Back face */
  .card-back { top: 623px; height: 574px; border-radius: 43px; background: var(--paper); }
  .holder-name {
    position: absolute; left: 70px; top: 82px;
    color: var(--brand-red); font-size: 41px; letter-spacing: 0.5px;
  }
  .holder-name .first { font-weight: 700; }
  .holder-name .last { font-weight: 400; }
  .back-brand {
    position: absolute; right: 68px; top: 70px;
    display: flex; align-items: center; gap: 12px;
  }
  .back-brand .brand-mark { width: 40px; height: 40px; }
  .back-brand .brand-name { font-size: 19px; }

  .contact-list { position: absolute; left: 67px; top: 328px; list-style: none; }
  .contact-item {
    display: flex; align-items: center; height: 51.5px;
    font-size: 20.5px; color: var(--ink);
  }
  .contact-icon { width: 32px; height: 32px; margin-right: 12px; flex: none; }
  .contact-icon * { fill: var(--brand-red); }
  .contact-icon .line { fill: none; stroke: var(--brand-red); stroke-width: 1.6; }
  .contact-icon .paper { fill: var(--paper); }

  .qr-spot {
    position: absolute; left: 662px; top: 363px; width: 145px; height: 145px;
    border: 2.5px solid var(--brand-red);
  }
</style>
</head>
<body>

<section class="card card-front">
  <div class="wood-panel wood-top" role="img" aria-label="Vertical wood plank panelling"></div>
  <div class="red-rule rule-top"></div>
  <div class="brand-band">
    <div class="brand-mark"></div>
    <div class="brand-name">Tallow Creek<br>Architectural Systems</div>
  </div>
  <div class="red-rule rule-bottom"></div>
  <div class="wood-panel wood-bottom" role="img" aria-label="Vertical wood plank panelling"></div>
</section>

<section class="card card-back">
  <h1 class="holder-name"><span class="first">NAME</span> <span class="last">HERE</span></h1>

  <div class="back-brand">
    <div class="brand-mark"></div>
    <div class="brand-name">Tallow Creek<br>Architectural Systems</div>
  </div>

  <ul class="contact-list">
    <li class="contact-item">
      <svg class="contact-icon" viewBox="0 0 32 32" aria-hidden="true">
        <path d="M6 3c2-1 4 0 5 2l2 4c1 2 0 3-1 4l-1 1c1 3 4 6 7 7l1-1c1-1 2-2 4-1l4 2c2 1 3 3 2 5l-1 2c-1 2-4 3-7 2C13 27 5 19 3 11 2 8 3 5 5 4z"/>
      </svg>
      +0123-456-789
    </li>
    <li class="contact-item">
      <svg class="contact-icon" viewBox="0 0 32 32" aria-hidden="true">
        <rect x="8" y="2" width="16" height="9"/>
        <rect x="1" y="10" width="30" height="13" rx="2"/>
        <rect x="7" y="18" width="18" height="12"/>
        <rect class="paper" x="9" y="21" width="14" height="1.4"/>
        <rect class="paper" x="9" y="24" width="14" height="1.4"/>
        <rect class="paper" x="9" y="27" width="14" height="1.4"/>
      </svg>
      +0123-456-789
    </li>
    <li class="contact-item">
      <svg class="contact-icon" viewBox="0 0 32 32" aria-hidden="true">
        <text x="16" y="26" text-anchor="middle" font-family="Carlito, sans-serif" font-weight="700" font-size="34">@</text>
      </svg>
      emailaddress@tallowcreekas.com
    </li>
    <li class="contact-item">
      <svg class="contact-icon" viewBox="0 0 32 32" aria-hidden="true">
        <circle cx="16" cy="16" r="15"/>
        <ellipse class="line" style="stroke:#fff" cx="16" cy="16" rx="6" ry="15"/>
        <line class="line" style="stroke:#fff" x1="16" y1="1" x2="16" y2="31"/>
        <line class="line" style="stroke:#fff" x1="1" y1="16" x2="31" y2="16"/>
        <line class="line" style="stroke:#fff" x1="4" y1="9" x2="28" y2="9"/>
        <line class="line" style="stroke:#fff" x1="4" y1="23" x2="28" y2="23"/>
      </svg>
      www.tallowcreekas.com
    </li>
  </ul>

  <div class="qr-spot" aria-label="QR code area"></div>
</section>

</body>
</html>
```